Veterinarian specialized in Equine (horse) sports medicine needs logo and stationary design!

New veterinary clinic only focused on horses needs logo and stationary designs. The clinic works with sport horses including jumping horses, dressage horses and polo horses (all disciplines you can find online. No racing horses). Name of clinic is StrideCare and is based in Mexico City where there is a large and elite clientele of sports horses. My main focus is orthopedics and rehabilitation.
I think logo should include horse(s), especially if they are performing a sport (like jumping, etc).

Target Market(s)

Elite horse-owners of sport horses.

Industry/Entity Type

Horseback Riding

Requirements
Must have
• Great Logo! I like bold and bright colors (no pastels), but with a professional tone.

```html
<!DOCTYPE html>
<html lang="en">
<head>
<meta charset="utf-8">
<title>StrideCare Stationery</title>
<link href="https://fonts.googleapis.com/css2?family=Quicksand:wght@400;500;700&display=swap" rel="stylesheet">
<style>
  :root {
    --sky: #3fb0df;
    --charcoal: #323032;
    --slate: #5f5e60;
    --paper: #f4f4f3;
    --backdrop: #e8e3db;
    --indigo: #3b3fa6;
    --footer-ink: #ececec;
    --watermark: #e3eef4;
  }
  * { margin: 0; padding: 0; box-sizing: border-box; }
  html, body { width: 1117px; height: 1200px; overflow: hidden; }
  body {
    background: var(--backdrop);
    font-family: "Quicksand", sans-serif;
    position: relative;
  }
  .sheet, .card {
    position: absolute;
    background: var(--paper);
    box-shadow: 0 6px 14px rgba(0,0,0,0.18);
    overflow: hidden;
  }
  .letterhead { left: 210px; top: 62px; width: 631px; height: 808px; }
  .wave { position: absolute; left: 0; top: 0; display: block; }
  .letterhead .wave { width: 631px; height: 190px; }
  .brand-name {
    position: absolute;
    font-family: "Quicksand", sans-serif;
    font-weight: 700;
    color: var(--charcoal);
    white-space: nowrap;
    letter-spacing: 0.5px;
  }
  .letterhead .brand-name { right: 52px; top: 130px; font-size: 34px; }
  .watermark {
    position: absolute; left: 88px; top: 240px; width: 460px; height: 400px;
    background: radial-gradient(ellipse at center, var(--watermark) 0%, rgba(227,238,244,0) 70%);
  }
  .footer-band {
    position: absolute; left: 0; bottom: 0; width: 100%; height: 46px;
    background: var(--charcoal);
    display: flex; align-items: center; justify-content: flex-end;
    gap: 12px; padding-right: 28px;
    color: var(--footer-ink); font-size: 17px; font-weight: 400;
  }
  .contact-item { display: flex; align-items: center; gap: 8px; }
  .contact-item svg { width: 15px; height: 15px; display: block; }
  .card { top: 941px; width: 270px; height: 162px; }
  .card-front { left: 225px; }
  .card-front .brand-name { left: 0; right: 0; text-align: center; top: 62px; font-size: 28px; color: var(--indigo); }
  .card-back { left: 552px; }
  .card-back .wave { width: 270px; height: 81px; }
  .card-back .brand-name { right: 22px; top: 56px; font-size: 17px; }
  .holder { position: absolute; left: 38px; top: 115px; }
  .holder-name { color: var(--sky); font-weight: 700; font-size: 12.5px; line-height: 1; }
  .holder-role { color: var(--charcoal); font-size: 8px; font-weight: 500; }
  .card-contacts {
    position: absolute; left: 148px; top: 110px; list-style: none;
    font-size: 7.5px; color: var(--charcoal); font-weight: 500;
  }
  .card-contacts li { display: flex; align-items: center; gap: 5px; height: 13px; }
  .dot { width: 5px; height: 5px; border-radius: 50%; background: var(--sky); }
</style>
</head>
<body>

<svg width="0" height="0" style="position:absolute">
  <defs>
    <symbol id="swoosh" viewBox="0 0 733 220" preserveAspectRatio="none">
      <path fill="var(--sky)" d="M0 0 H733 V8 C620 0 520 30 440 80 C340 140 200 160 0 152 Z"/>
      <path fill="var(--slate)" d="M0 185 C200 190 360 168 470 100 C500 82 520 70 545 60 C470 112 380 172 260 196 C170 213 80 216 0 212 Z"/>
      <path fill="var(--charcoal)" d="M0 152 C200 160 340 140 440 80 C520 30 620 0 733 8 V30 C640 20 560 45 470 100 C360 168 200 190 0 185 Z"/>
    </symbol>
  </defs>
</svg>

<section class="sheet letterhead">
  <svg class="wave" preserveAspectRatio="none"><use href="#swoosh"/></svg>
  <div class="brand-name">StrideCare</div>
  <div class="watermark" role="img" aria-label="Faint brand watermark area"></div>
  <footer class="footer-band">
    <span class="contact-item">
      <svg viewBox="0 0 16 16"><rect x="4" y="1" width="8" height="14" rx="1.5" fill="none" stroke="currentColor" stroke-width="1.6"/><circle cx="8" cy="12.5" r="0.9" fill="currentColor"/></svg>
      000.222.5678
    </span>
    <span class="contact-item">
      <svg viewBox="0 0 16 16"><text x="8" y="12.5" text-anchor="middle" font-size="14" font-weight="700" fill="currentColor" font-family="Quicksand, sans-serif">@</text></svg>
      info@stridecare.com
    </span>
    <span class="contact-item">
      <svg viewBox="0 0 16 16" fill="none" stroke="currentColor" stroke-width="1.3"><circle cx="8" cy="8" r="6.5"/><ellipse cx="8" cy="8" rx="2.8" ry="6.5"/><path d="M1.5 8 H14.5 M2.5 5 H13.5 M2.5 11 H13.5"/></svg>
      www.stridecare.com
    </span>
  </footer>
</section>

<section class="card card-front">
  <div class="brand-name">StrideCare</div>
</section>

<section class="card card-back">
  <svg class="wave" preserveAspectRatio="none"><use href="#swoosh"/></svg>
  <div class="brand-name">StrideCare</div>
  <div class="holder">
    <div class="holder-name">Ana Ruiz</div>
    <div class="holder-role">Director</div>
  </div>
  <ul class="card-contacts">
    <li><span class="dot"></span>000.222.5678</li>
    <li><span class="dot"></span>info@stridecare.com</li>
    <li><span class="dot"></span>www.stridecare.com</li>
  </ul>
</section>

</body>
</html>
```